TK Joinery

Cabinet maker. Kitchens. Wardrobes. Vanitys. Entertainment units

Target Market(s)

Modern contemporary.geometry. colours black, gray, charcoal and orange. Matt card gloss letters

Industry/Entity Type

Entertainment

Contact Information for Business Card

Mattias Velder 0418 295 437
mattias.velder@fernmail.test
ABN 471 9052 8316

Font styles to use
Decorative

Colors
000000

Requirements
Should not have
• Pictures

```html
<!DOCTYPE html>
<html lang="en">
<head>
<meta charset="utf-8">
<title>TK Joinery – Business Card</title>
<link rel="stylesheet" href="https://fonts.googleapis.com/css2?family=Almendra:wght@400;700&family=Alegreya+Sans:wght@500;700&display=swap">
<style>
  :root {
    --page: #e7e3dd;
    --card-black: #000000;
    --charcoal: #1c1c1c;
    --grain-light: #4a4a4a;
    --bar-gray: #858585;
    --ink-white: #ffffff;
    --ink-soft: #e4e4e4;
  }
  html, body {
    margin: 0;
    padding: 0;
    width: 1200px;
    height: 1200px;
    overflow: hidden;
    background: var(--page);
  }
  .canvas {
    position: relative;
    width: 1200px;
    height: 1200px;
    background: var(--page);
  }
  .card {
    position: absolute;
    left: 160px;
    width: 880px;
    height: 500px;
    background: var(--card-black);
    box-shadow: 0 6px 18px rgba(0,0,0,0.25);
    overflow: hidden;
  }
  .card--front { top: 70px; }
  .card--back { top: 630px; }

  .front__grain {
    position: absolute;
    inset: 0;
    background: radial-gradient(ellipse 60% 55% at 50% 45%, var(--grain-light) 0%, var(--charcoal) 55%, var(--card-black) 100%);
  }
  .front__content {
    position: absolute;
    inset: 0;
    display: flex;
    flex-direction: column;
    align-items: center;
    justify-content: center;
    padding-bottom: 10px;
  }
  .wordmark {
    font-family: "Almendra", serif;
    font-weight: 700;
    font-size: 78px;
    letter-spacing: 4px;
    text-transform: uppercase;
    color: var(--ink-white);
    margin: 0 0 40px 0;
    line-height: 1;
  }
  .services {
    font-family: "Almendra", serif;
    font-weight: 700;
    font-size: 28px;
    color: var(--ink-soft);
    text-align: center;
    line-height: 1.2;
    margin: 0;
  }
  .services .sep { margin: 0 10px; }

  .back__bars {
    position: absolute;
    inset: 0;
  }
  .holder-name {
    position: absolute;
    left: 105px;
    top: 68px;
    margin: 0;
    font-family: "Alegreya Sans", sans-serif;
    font-weight: 700;
    font-size: 58px;
    color: var(--ink-white);
  }
  .contact {
    position: absolute;
    right: 92px;
    top: 262px;
    margin: 0;
    padding: 0;
    list-style: none;
    font-family: "Alegreya Sans", sans-serif;
    font-weight: 500;
    font-size: 27px;
    color: var(--ink-white);
  }
  .contact__item {
    display: flex;
    justify-content: flex-end;
    align-items: center;
    height: 56px;
  }
  .contact__icon {
    width: 26px;
    height: 26px;
    margin-left: 28px;
    flex: none;
  }
</style>
</head>
<body>
<main class="canvas">

  <section class="card card--front">
    <div class="front__grain" role="img" aria-label="Dark charcoal wood grain texture lit softly at the centre"></div>
    <div class="front__content">
      <h1 class="wordmark">TK Joinery</h1>
      <p class="services">
        Cabinet maker<span class="sep">|</span>Kitchens<span class="sep">|</span>Wardrobes<br>
        Vanitys<span class="sep">|</span>Entertainment units
      </p>
    </div>
  </section>

  <section class="card card--back">
    <svg class="back__bars" width="880" height="500" viewBox="0 0 880 500" aria-hidden="true">
      <g stroke="var(--bar-gray)" stroke-width="15" stroke-linecap="round" fill="none">
        <line x1="-20" y1="290" x2="180" y2="222"/>
        <line x1="-20" y1="342" x2="185" y2="272"/>
        <line x1="-20" y1="394" x2="190" y2="322"/>
        <line x1="-20" y1="446" x2="195" y2="372"/>
        <line x1="745" y1="90" x2="900" y2="28"/>
        <line x1="570" y1="222" x2="900" y2="90"/>
      </g>
    </svg>

    <h2 class="holder-name">Mattias Velder</h2>

    <ul class="contact">
      <li class="contact__item">
        <span>0418 295 437</span>
        <svg class="contact__icon" viewBox="0 0 24 24" aria-hidden="true">
          <path fill="var(--ink-white)" d="M8 3c-1 0-2.5 1.5-2.5 3 0 6 6.5 13 12.5 13 1.5 0 3-1.3 3-2.3l-3.2-2.7-2 1.6c-2-1-4.5-3.5-5.5-5.5l1.6-2L8 3z"/>
        </svg>
      </li>
      <li class="contact__item">
        <span>mattias.velder@fernmail.test</span>
        <svg class="contact__icon" viewBox="0 0 24 24" aria-hidden="true">
          <text x="12" y="19" text-anchor="middle" font-family="Alegreya Sans, sans-serif" font-weight="700" font-size="22" fill="var(--ink-white)">@</text>
        </svg>
      </li>
      <li class="contact__item">
        <span>ABN 471 9052 8316</span>
        <svg class="contact__icon" viewBox="0 0 24 24" aria-hidden="true">
          <path fill="var(--ink-white)" fill-rule="evenodd" d="M12 2a7 7 0 0 0-7 7c0 5 7 13 7 13s7-8 7-13a7 7 0 0 0-7-7zm0 4a3 3 0 1 1 0 6 3 3 0 0 1 0-6z"/>
        </svg>
      </li>
    </ul>
  </section>

</main>
</body>
</html>
```